Credit card acceptance poster

I need a poster explaining to my customers that the washers and dryers at my laundromat accept credit card payments and most mobile wallet payments. I have attached a flyer I made. It looks terrible so I need help. The cc readers accept: NORO, BRUNOVAULT, TALVEXIA, HOLBORNE TRAMLEY, ZORBIT PAY, WENDLE PAY, AND KIRUVEX PAY.

Colors
0054AA
0677BA
7BADD7
CADEEF
E8F1F8

```html
<!DOCTYPE html>
<html lang="en">
<head>
<meta charset="utf-8">
<title>Card Payments Poster</title>
<link rel="stylesheet" href="https://fonts.googleapis.com/css2?family=Montserrat:wght@500;700;800&display=swap">
<style>
  :root {
    --navy: #0054AA;
    --ink: #0b4a94;
    --blue: #0677BA;
    --bright: #0a8fd6;
    --sky: #7BADD7;
    --aqua: #79c5e3;
    --pale: #CADEEF;
    --mist: #E8F1F8;
    --page: #eeeeee;
    --white: #ffffff;
  }
  * { margin: 0; padding: 0; box-sizing: border-box; }
  html, body { width: 1200px; height: 727px; overflow: hidden; background: var(--page); }
  body { font-family: "Montserrat", sans-serif; position: relative; }

  .poster {
    position: absolute; left: 403px; top: 86px;
    width: 393px; height: 555px; overflow: hidden; background: var(--white);
  }
  .poster-shapes { position: absolute; inset: 0; }

  .headline {
    position: absolute; left: 6px; top: 48px; width: 200px;
    text-align: center; color: var(--ink);
    font-weight: 800; font-size: 26px; line-height: 33px; letter-spacing: -0.4px;
  }
  .reassure {
    position: absolute; left: 17px; top: 184px; width: 165px; height: 54px;
    border-radius: 14px; background: var(--bright); color: var(--white);
    font-weight: 800; font-size: 20px; line-height: 54px; text-align: center;
  }
  .body-copy {
    position: absolute; left: 33px; top: 332px; width: 215px;
    color: var(--ink); font-weight: 500; font-size: 15.5px; line-height: 19.6px;
  }
  .brand {
    position: absolute; left: 234px; top: 455px; display: flex; align-items: center; gap: 7px;
    color: var(--navy); font-weight: 800;
  }
  .brand-dot { width: 16px; height: 16px; border-radius: 50%; background: var(--navy); flex: none; }
  .brand-name { display: block; font-size: 17px; line-height: 18px; }
  .brand-name small { display: block; font-size: 11px; line-height: 13px; letter-spacing: 1.8px; }

  .payments {
    position: absolute; left: 27px; top: 514px; display: flex; gap: 7.5px; list-style: none;
  }
  .payment {
    width: 42px; height: 27px; background: var(--white); border-radius: 2px;
    display: flex; align-items: center; justify-content: center; text-align: center;
    color: var(--ink); font-weight: 800; font-size: 6px; line-height: 7px;
  }
</style>
</head>
<body>
  <main class="poster">
    <svg class="poster-shapes" width="393" height="555" viewBox="0 0 393 555">
      <defs>
        <linearGradient id="sky-wash" x1="0" y1="0" x2="0" y2="1">
          <stop offset="0" stop-color="#1a93d3"/>
          <stop offset="1" stop-color="#8dd0ea"/>
        </linearGradient>
        <linearGradient id="footer-wash" x1="0" y1="0" x2="0" y2="1">
          <stop offset="0" stop-color="#7cc6e4"/>
          <stop offset="0.72" stop-color="#62b8e1"/>
          <stop offset="1" stop-color="#1685cc"/>
        </linearGradient>
        <linearGradient id="photo-tone" x1="0" y1="0" x2="0" y2="1">
          <stop offset="0" stop-color="#fafafa"/>
          <stop offset="0.45" stop-color="#e9ebee"/>
          <stop offset="0.62" stop-color="#5a5d63"/>
          <stop offset="1" stop-color="#1f2126"/>
        </linearGradient>
        <linearGradient id="splash-tone" x1="0" y1="0" x2="1" y2="1">
          <stop offset="0" stop-color="#2f9ad6" stop-opacity="0.55"/>
          <stop offset="0.5" stop-color="#0a7fc6"/>
          <stop offset="1" stop-color="#1e8fd0" stop-opacity="0.8"/>
        </linearGradient>
        <linearGradient id="machine-tone" x1="0" y1="0" x2="1" y2="0">
          <stop offset="0" stop-color="#b9bcc0"/>
          <stop offset="0.45" stop-color="#8c9095"/>
          <stop offset="1" stop-color="#55595e"/>
        </linearGradient>
        <clipPath id="poster-clip"><rect width="393" height="555"/></clipPath>
      </defs>

      <g clip-path="url(#poster-clip)">
        <polygon class="top-band" points="0,0 240,0 216,34 0,34" fill="var(--blue)"/>
        <polygon class="sky-section" points="0,122 393,122 393,271 0,298" fill="url(#sky-wash)"/>

        <circle class="photo" cx="316" cy="70" r="118" fill="url(#photo-tone)" role="img"
                aria-label="Photo of a man in a white shirt pulling out his empty trouser pockets"/>

        <path class="splash" role="img" aria-label="Illustration of a blue water splash wrapping the photo"
              d="M178 150 C196 196 250 214 300 202 C340 193 372 170 393 150
                 L393 226 C372 258 336 276 292 278 C246 280 214 262 200 236
                 C190 218 184 186 178 150 Z"
              fill="url(#splash-tone)"/>

        <polygon class="machine" points="259,283 393,270 393,435 259,437" fill="url(#machine-tone)" role="img"
                 aria-label="Photo of a card payment terminal machine"/>

        <polygon class="footer-section" points="0,461 393,424 393,555 0,555" fill="url(#footer-wash)"/>
      </g>
    </svg>

    <h1 class="headline">“NO BILLS OR COINS”</h1>
    <div class="reassure">No Problem!</div>

    <p class="body-copy">Our machines accept<br>Credit card payments<br>And most mobile<br>Wallet applications.</p>

    <div class="brand">
      <span class="brand-dot"></span>
      <span class="brand-name">SUDS CROWN<small>LAUNDROMAT</small></span>
    </div>

    <ul class="payments" aria-label="Accepted payments">
      <li class="payment">TALVEXIA</li>
      <li class="payment">BRUNO<br>VAULT</li>
      <li class="payment">KIRUVEX<br>PAY</li>
      <li class="payment">WENDLE<br>PAY</li>
      <li class="payment">ZORBIT<br>PAY</li>
      <li class="payment">HOLBORNE<br>TRAMLEY</li>
      <li class="payment">NORO</li>
    </ul>
  </main>
</body>
</html>
```